Business Card Design - Law Firm

We are a boutique law firm located near the beach in Manly, Australia. We have recently had a new logo designed and are revamping our business cards with the new logo.

We have recently had a business card design done for us but are not entirely happy with it. We are looking for something modern, simplistic but striking. We would like to see multiple designs.

We have attached a word document which includes our new logo and the current business card design which we are looking at moving away from.

We would like the business cards to be double sided. We would like the design to include something which we can print in gloss colour when we send it to the business card printers.

```html
<!DOCTYPE html>
<html lang="en">
<head>
<meta charset="utf-8">
<title>Harbourne &amp; Partners – Business Card</title>
<link href="https://fonts.googleapis.com/css2?family=Roboto:wght@400;500;700&display=swap" rel="stylesheet">
<style>
  :root {
    --backdrop: #bcbcbc;
    --card: #f4f4f3;
    --navy: #1b2a6b;
    --blue: #4d72b0;
    --gold: #a89a70;
    --ink: #222428;
    --ink-soft: #3a3c40;
  }
  * { box-sizing: border-box; margin: 0; padding: 0; }
  html, body { width: 1200px; height: 576px; overflow: hidden; }
  body {
    background: var(--backdrop);
    font-family: 'Roboto', Arial, sans-serif;
    color: var(--ink);
    position: relative;
  }
  .card {
    position: absolute;
    top: 138px;
    width: 484px;
    height: 294px;
    background: var(--card);
    border-radius: 12px;
    overflow: hidden;
  }
  .card--front { left: 82px; }
  .card--back { left: 602px; }

  /* Front */
  .brand {
    display: flex;
    align-items: center;
    gap: 10px;
    font-weight: 500;
    color: var(--ink);
    letter-spacing: 1.2px;
  }
  .brand__dot {
    width: 14px; height: 14px;
    border-radius: 50%;
    background: var(--navy);
    flex: none;
  }
  .card--front .brand {
    position: absolute;
    left: 0; right: 0;
    top: 162px;
    justify-content: center;
    font-size: 22px;
  }
  .front-web {
    position: absolute;
    left: 0; right: 0;
    top: 251px;
    display: flex;
    align-items: center;
    justify-content: center;
    gap: 14px;
    font-size: 13px;
    color: var(--ink-soft);
  }
  .front-web__rule {
    width: 50px; height: 2px;
    background: linear-gradient(90deg, transparent, var(--blue));
  }
  .front-web__rule--right { background: linear-gradient(90deg, var(--blue), transparent); }
  .front-band {
    position: absolute;
    left: 0; right: 0; bottom: 0;
    height: 13px;
    display: flex;
  }
  .front-band__blue { flex: 1; background: linear-gradient(90deg, var(--navy), var(--blue)); }
  .front-band__gold { flex: 1; background: linear-gradient(90deg, #8f8463, var(--gold)); }

  /* Back */
  .card--back .brand {
    position: absolute;
    left: 30px;
    top: 110px;
    font-size: 14px;
    gap: 8px;
  }
  .card--back .brand__dot { width: 11px; height: 11px; }
  .holder {
    position: absolute;
    right: 27px;
    top: 122px;
    text-align: right;
  }
  .holder__name {
    font-size: 21px;
    font-weight: 700;
    color: var(--navy);
  }
  .holder__role {
    font-size: 12px;
    margin-top: 5px;
    color: var(--ink);
  }
  .back-rule {
    position: absolute;
    left: 30px; right: 27px;
    top: 187px;
    height: 1.5px;
    background: var(--gold);
  }
  .contacts {
    position: absolute;
    left: 30px;
    top: 203px;
    list-style: none;
    font-size: 12.5px;
    line-height: 18.5px;
  }
  .contacts li { display: flex; align-items: center; gap: 9px; }
  .contacts svg { width: 11px; height: 11px; fill: var(--navy); flex: none; }
  .address {
    position: absolute;
    right: 27px;
    top: 240px;
    text-align: right;
    font-size: 12.5px;
    line-height: 18.5px;
    font-style: normal;
  }
</style>
</head>
<body>

<section class="card card--front" aria-label="Card front">
  <div class="brand"><span class="brand__dot"></span>Harbourne &amp; Partners</div>
  <div class="front-web">
    <span class="front-web__rule"></span>
    <span>www.harbourneandpartners.com.au</span>
    <span class="front-web__rule front-web__rule--right"></span>
  </div>
  <div class="front-band"><span class="front-band__blue"></span><span class="front-band__gold"></span></div>
</section>

<section class="card card--back" aria-label="Card back">
  <div class="brand"><span class="brand__dot"></span>Harbourne &amp; Partners</div>
  <div class="holder">
    <div class="holder__name">Elise Marwood</div>
    <div class="holder__role">Managing Director</div>
  </div>
  <div class="back-rule"></div>
  <ul class="contacts">
    <li><svg viewBox="0 0 12 12"><path d="M1 4c0-2 2-3 5-3s5 1 5 3v1H8.5V3.6C7.8 3.3 4.2 3.3 3.5 3.6V5H1z"/><path d="M2.5 6h7l1 5h-9z"/></svg>(02) 9410 3386</li>
    <li><svg viewBox="0 0 12 12"><path d="M1 4c0-2 2-3 5-3s5 1 5 3v1H8.5V3.6C7.8 3.3 4.2 3.3 3.5 3.6V5H1z"/><path d="M2.5 6h7l1 5h-9z"/></svg>(02) 9410 3387</li>
    <li><svg viewBox="0 0 12 12"><path d="M0.5 2.5h11v7h-11z M1.5 3.3 6 6.8l4.5-3.5" stroke="#f4f4f3" stroke-width="0.8"/></svg>elise.marwood@harbournelaw.com.au</li>
    <li><svg viewBox="0 0 12 12"><circle cx="6" cy="6" r="5"/><path d="M1 6h10M6 1v10M6 1c-2.6 2.8-2.6 7.2 0 10M6 1c2.6 2.8 2.6 7.2 0 10" stroke="#f4f4f3" stroke-width="0.7" fill="none"/></svg>www.harbourneandpartners.com.au</li>
  </ul>
  <address class="address">Suite 4, 18 Coral Street<br>Brookvale NSW 2100</address>
</section>

</body>
</html>
```